Website Redesign - We Need Your Magic!

Hello we are looking for you to help us re-design a high end and professional website for a high-end private school.

Here is the current site: http://www.veltrasham.example/

NOTE THIS IS DESIGN ONLY, NO CODING :)

The image they want to portray is that of high quality sports and education, in a creative "un-stiff" way.

Menu Bar: Horizontal

Look and Feel:

Site Colors: Dark green and a Gold yellow (logos are attached)

This site will represent a school so the look must be clean, bold, and classy. The site must have a very clean user interface, with things easily recognizable. Think simple.

The site should be visually appealing! If you come to me with templates, or a ton of text you will be out.

This site should be outside the box, we do not want boring, we do not want status quo. This site should instill excitement, innovation, and athletics.

So the main points again are:

1. High-end and classy look, with creative feel
2. Simple and clear navigation style
3. To cover the Junior and High School - Veltrasham College Schools

Think outside the box. We look forward to seeing what you come up with!!

Thank you for helping us create an amazing site for the school!

Industry/Entity Type

School

```html
<!DOCTYPE html>
<html lang="en">
<head>
<meta charset="utf-8">
<title>Veltrasham College</title>
<link href="https://fonts.googleapis.com/css2?family=Open+Sans:wght@400;600;700&family=Arimo:wght@400;700&display=swap" rel="stylesheet">
<style>
:root{
  --green:#0b4d1f;
  --green-dark:#083d18;
  --green-soft:#2e6b3f;
  --gold:#c9c21c;
  --gold-deep:#d4a90c;
  --ink:#222;
  --body:#333;
  --paper:#f6f6f6;
  --footer:#232323;
  --footer-base:#141414;
}
*{box-sizing:border-box;margin:0;padding:0}
html,body{width:800px;height:1200px;overflow:hidden}
body{position:relative;background:#fff;font-family:"Arimo",Arial,sans-serif;color:var(--body)}
.abs{position:absolute}

/* header */
.site-header{position:absolute;left:0;top:0;width:800px;height:130px;background:var(--paper)}
.crest{left:82px;top:16px}
.brand-name{left:183px;top:52px;font-family:"Open Sans",sans-serif;font-weight:700;font-size:26px;color:var(--green);letter-spacing:.3px}
.brand-tag{left:186px;top:88px;font-family:"Open Sans",sans-serif;font-weight:600;font-size:12px;color:#333}
.contact-line{left:576px;font-size:11px;color:#111;display:flex;align-items:center;gap:8px}
.contact-line svg{flex:none}
.contact-phone{top:45px;font-weight:700}
.contact-mail{top:64px;text-decoration:underline}
.search{left:572px;top:94px;width:144px;height:24px;display:flex}
.search-field{flex:1;background:#fff;border:1px solid #d6d6d6;font-size:8px;color:#999;padding:8px 7px}
.search-go{width:32px;background:#151515;color:#fff;font-size:11px;font-weight:700;display:flex;align-items:center;justify-content:center}

/* navigation */
.main-nav{position:absolute;left:0;top:130px;width:800px;height:32px;background:var(--green);border-bottom:1px solid #0e5a26}
.nav-item{position:absolute;top:0;height:32px;line-height:32px;font-size:9.5px;color:#fff;transform:translateX(-50%);white-space:nowrap}
.nav-home{left:76px;top:7px;width:64px;height:21px;background:var(--gold);color:#222;line-height:21px;text-align:center;transform:none}
.nav-sep{position:absolute;top:8px;width:1px;height:18px;background:#1f6a35}

/* hero */
.hero{position:absolute;left:0;top:162px;width:800px;height:252px;border-bottom:2px solid var(--green)}
.hero-panel{position:absolute;top:0;height:250px}
.p1{left:0;width:266px;background:linear-gradient(160deg,#5b6b4a,#8b8a7d 45%,#4c4f52)}
.p2{left:267px;width:266px;background:linear-gradient(170deg,#4f6b3f,#9aa870 55%,#7d9b5a)}
.p3{left:534px;width:266px;background:linear-gradient(165deg,#3c4656,#9aa2ad 50%,#e8ecf0)}
.hero-caption{position:absolute;left:474px;top:172px;width:249px;height:58px;background:rgba(15,15,15,.85);text-align:center;font-family:"Open Sans",sans-serif;font-weight:600}
.hero-caption .t1{font-size:20px;color:#fff;margin-top:3px}
.hero-caption .t2{font-size:15px;color:var(--gold);margin-top:-2px}
.hero-dot{position:absolute;left:297px;top:239px;width:10px;height:10px;border-radius:50%;background:#fff}

/* main content */
.section-title{font-family:"Arimo",sans-serif;font-weight:700;font-size:18px;color:var(--ink);letter-spacing:.2px}
.copy p{font-size:8.6px;line-height:13.5px;margin-bottom:13px;color:#333}
.copy strong{color:#111}
.welcome-title{left:75px;top:440px}
.welcome-copy{left:77px;top:476px;width:395px}
.welcome-copy .hl{color:var(--green);font-weight:700}
.head-title{left:75px;top:666px;font-size:15px}
.head-photo{left:75px;top:707px;width:96px;height:83px;border:3px solid #ddd;background:linear-gradient(160deg,#1d5a2e,#6d7b57 55%,#c9b08e)}
.head-lead{left:184px;top:704px;width:290px}
.head-rest{left:74px;top:826px;width:400px}

/* sidebar */
.signup{left:526px;top:446px;width:199px;height:174px;background:var(--green);border-radius:3px;padding:10px 10px}
.signup h2{font-family:"Open Sans",sans-serif;font-weight:600;font-size:17px;color:#fff;letter-spacing:.6px}
.signup p{font-size:8.4px;line-height:12px;color:#d9e4d6;margin-top:4px}
.signup-field{width:167px;height:23px;background:#fff;font-size:8px;color:#888;padding:7px 6px;margin-top:11px}
.signup-field + .signup-field{margin-top:12px}
.signup-btn{width:97px;height:23px;margin-top:8px;background:var(--gold-deep);color:#1a1a1a;font-family:"Open Sans",sans-serif;font-weight:600;font-size:12px;line-height:23px;text-align:center;border-radius:2px;letter-spacing:.3px}
.events-title{left:524px;top:646px;font-family:"Open Sans",sans-serif;font-weight:600;font-size:15px;color:var(--ink);letter-spacing:.6px}
.events-rule{left:524px;top:673px;width:201px;height:3px;background:var(--green)}
.events-rule i{display:block;width:32px;height:3px;background:var(--gold)}
.event{left:528px;width:189px;font-size:8.6px;color:#333;padding:0 0 8px 11px;border-bottom:1px solid #e5e5e5;white-space:nowrap;overflow:hidden}
.event::before{content:"";position:absolute;left:0;top:3px;border-left:4px solid #222;border-top:3px solid transparent;border-bottom:3px solid transparent}
.more-events{left:656px;top:737px;font-size:8.6px;color:var(--green)}

.feed-box{left:530px;top:771px;width:190px;height:206px;border:1px solid #c9d2c9;background:#fff;font-size:7px;color:#333}
.feed-head{height:22px;background:var(--green-soft);color:#fff;display:flex;align-items:center;padding:0 6px;font-size:7.5px}
.feed-page{display:flex;gap:6px;padding:5px 5px;border-bottom:1px solid #e3e3e3}
.feed-badge{width:22px;height:22px;border-radius:50%;background:var(--green);flex:none}
.feed-badge.grey{background:#c4c4c4}
.feed-name{color:var(--green-soft);font-size:8.5px}
.feed-like{margin-top:4px;display:flex;gap:4px;align-items:center;font-size:6.5px}
.feed-like span{border:1px solid #ccc;padding:1px 3px;color:#999}
.feed-post{display:flex;gap:6px;padding:6px 14px 6px 5px;height:78px;border-bottom:1px solid #e3e3e3;position:relative}
.feed-post .quote{font-size:7.3px;margin-top:2px}
.feed-link{margin-top:5px;border-left:1px solid #ccc;padding-left:5px;font-size:6px;color:#666}
.feed-link b{display:block;color:var(--green-soft);font-size:6.8px}
.feed-scroll{position:absolute;right:2px;top:4px;width:6px;height:70px;border:1px solid #ddd;background:#f2f2f2}
.feed-count{padding:4px 5px 3px;font-size:6.8px}
.feed-faces{display:flex;gap:5px;padding:0 5px}
.feed-face{width:31px;height:31px;background:linear-gradient(160deg,#8a7565,#c7b3a0)}
.feed-foot{margin:5px 5px 0;padding-top:3px;border-top:1px solid #e3e3e3;font-size:5.8px;color:var(--green-soft);display:flex;gap:3px;align-items:center}
.feed-foot i{width:7px;height:7px;background:#999;display:block}

/* footer */
.site-footer{position:absolute;left:0;top:1032px;width:800px;height:140px;background:var(--footer)}
.foot-pin{left:74px;top:35px}
.foot-name{left:121px;top:40px;font-family:"Open Sans",sans-serif;font-weight:600;font-size:12.5px;color:#eee;letter-spacing:.3px}
.foot-addr{left:121px;top:59px;width:116px;text-align:right;font-size:7.8px;line-height:12px;color:#ddd}
.foot-dir{left:116px;top:86px;width:121px;text-align:right;font-size:7.8px;color:#ddd;text-decoration:underline}
.foot-div{top:25px;width:0;height:92px;border-left:1px dashed #444}
.follow-title{left:338px;top:32px;font-family:"Open Sans",sans-serif;font-weight:600;font-size:11.5px;color:#eee;letter-spacing:.5px}
.social{top:72px;display:flex;align-items:center}
.social i{width:24px;height:24px;border-radius:50%;background:#555;border:2px solid #d8d8d8;display:block}
.partner{background:#4a4a4a;border-radius:3px}
.foot-seal{left:680px;top:47px;width:42px;height:42px;border-radius:50%;background:#d0d0d0}
.copyright{position:absolute;left:0;top:1172px;width:800px;height:28px;background:var(--footer-base);color:#ddd;font-size:8px;text-align:center;line-height:28px}
</style>
</head>
<body>

<header class="site-header">
  <svg class="abs crest" width="88" height="88" viewBox="0 0 88 88" aria-hidden="true">
    <circle cx="44" cy="44" r="40" fill="#0b4d1f"/>
  </svg>
  <div class="abs brand-name">Veltrasham College</div>
  <div class="abs brand-tag">Stepping Ahead in Education, Culture, Sport &amp; Life</div>

  <div class="abs contact-line contact-phone">
    <svg width="13" height="13" viewBox="0 0 24 24" aria-hidden="true"><path d="M6.6 10.8a15.2 15.2 0 0 0 6.6 6.6l2.2-2.2c.3-.3.7-.4 1-.2 1.1.4 2.3.6 3.6.6.6 0 1 .4 1 1V20c0 .6-.4 1-1 1A17 17 0 0 1 3 4c0-.6.4-1 1-1h3.5c.6 0 1 .4 1 1 0 1.3.2 2.5.6 3.6.1.3 0 .7-.2 1z" fill="#222"/></svg>
    <span>0770 555 010 / 0770 555 020</span>
  </div>
  <div class="abs contact-line contact-mail">
    <svg width="14" height="10" viewBox="0 0 14 10" aria-hidden="true"><rect x=".5" y=".5" width="13" height="9" fill="none" stroke="#222"/><path d="M.5.5 7 6 13.5.5" fill="none" stroke="#222"/></svg>
    <span>admin@veltrasham.example</span>
  </div>

  <div class="abs search">
    <div class="search-field">Search....</div>
    <div class="search-go">GO</div>
  </div>
</header>

<nav class="main-nav">
  <div class="nav-item nav-home">HOME</div>
  <span class="nav-sep" style="left:165px"></span>
  <div class="nav-item" style="left:206px">ABOUT US</div>
  <span class="nav-sep" style="left:248px"></span>
  <div class="nav-item" style="left:289px">ACADEMICS</div>
  <span class="nav-sep" style="left:330px"></span>
  <div class="nav-item" style="left:370px">SPORTS</div>
  <span class="nav-sep" style="left:412px"></span>
  <div class="nav-item" style="left:478px">JOINING VELTRASHAM</div>
  <span class="nav-sep" style="left:540px"></span>
  <div class="nav-item" style="left:585px">ABOUT US</div>
  <span class="nav-sep" style="left:628px"></span>
  <div class="nav-item" style="left:676px">CONTACT US</div>
</nav>

<section class="hero">
  <div class="hero-panel p1" role="img" aria-label="Photo of students playing basketball"></div>
  <div class="hero-panel p2" role="img" aria-label="Photo of girls playing field hockey"></div>
  <div class="hero-panel p3" role="img" aria-label="Photo of horse racing in the snow"></div>
  <div class="hero-caption">
    <div class="t1">Quality Education</div>
    <div class="t2">A Community Commitment</div>
  </div>
  <span class="hero-dot"></span>
</section>

<main>
  <h1 class="abs section-title welcome-title">Welcome to Veltrasham College</h1>
  <div class="abs copy welcome-copy">
    <p>Welcome to <span class="hl">Veltrasham Group of Schools</span> where our School Motto is ‘Tabatana’ meaning Togetherness. We aim to work together in every aspect of School life, from academics to sport.</p>
    <p>Veltrasham College opened on 14th February 1983 and occupies 120 ha of land amidst the low hills of the Orvane Range, 8km west of Kestrow. This location encourages focus on School life away from the distractions and hustle and bustle of the larger towns.</p>
    <p>The day scholars have the option of selected bus drop off points for parents to collect day scholars closer to home.</p>
    <p>Veltrasham College offers a wide range of academic subjects alongside a varied sport and extra-curricular program.</p>
  </div>

  <h2 class="abs section-title head-title">Headmaster's Message</h2>
  <div class="abs head-photo" role="img" aria-label="Portrait of the headmaster"></div>
  <div class="abs copy head-lead">
    <p><strong>Welcome to Veltrasham College. Here at the College we aim to encourage each pupil to be a self-confident, well-rounded individual.</strong></p>
    <p>We aim to propel them to the highest level of achievement in both academics and extra-curricular activities to provide them with the life skills they will need when they leave the College and to prepare them to be of value to society.</p>
  </div>
  <div class="abs copy head-rest">
    <p>The College is a warm community which lives out high standards and is rightly proud of its achievements.</p>
    <p>We are a small enough School for each pupil to be known well, but large enough to offer a wide range of subjects and experience.Our Website covers many aspects of the College from how to apply for a place, to the curriculum and to much more. I hope you find it helpful and interesting.</p>
    <p>Please visit and meet the pupils, the staff and see for yourself what Veltrasham College can offer your son or daughter.</p>
    <p><strong>I look forward to welcoming you and your family to Veltrasham College.</strong></p>
  </div>
</main>

<aside>
  <form class="abs signup">
    <h2>Email Sign Up</h2>
    <p>If you would like to be added to the list of parents that receive the School Newsletter,</p>
    <div class="signup-field">Enter Your name</div>
    <div class="signup-field">Enter Your email</div>
    <div class="signup-btn">SUBSCRIBE</div>
  </form>

  <h2 class="abs events-title">Upcoming Events</h2>
  <div class="abs events-rule"><i></i></div>
  <div class="abs event" style="top:692px">Robotic competitions teach students</div>
  <div class="abs event" style="top:717px;border-bottom:0">Robotic competitions teach students how to</div>
  <div class="abs more-events">More Events...</div>

  <div class="abs feed-box">
    <div class="feed-head">Find us on Friendbook</div>
    <div class="feed-page">
      <span class="feed-badge"></span>
      <div>
        <div class="feed-name">Campus Chatter</div>
        <div class="feed-like"><span>✓ Like</span> You like this.</div>
      </div>
    </div>
    <div class="feed-post">
      <span class="feed-badge grey"></span>
      <div>
        <div class="feed-name">Campus Chatter</div>
        <div class="quote">"The idea of a culinary contest one either."</div>
        <div class="feed-link"><b>Social Media Campaign</b>www.campuschatter.example<br>Harvest Kitchen recipe book.</div>
      </div>
      <span class="feed-scroll"></span>
    </div>
    <div class="feed-count">30,821 people like <b>Campus Chatter</b>.</div>
    <div class="feed-faces" role="img" aria-label="Small profile photos of followers">
      <span class="feed-face"></span><span class="feed-face"></span><span class="feed-face"></span><span class="feed-face"></span><span class="feed-face"></span>
    </div>
    <div class="feed-foot"><i></i>Friendbook social plugin</div>
  </div>
</aside>

<footer class="site-footer">
  <svg class="abs foot-pin" width="30" height="42" viewBox="0 0 30 42" aria-hidden="true"><path d="M15 0C6.7 0 0 6.7 0 15c0 11 15 27 15 27s15-16 15-27C30 6.7 23.3 0 15 0z" fill="#8a8a8a"/><circle cx="15" cy="15" r="5" fill="#232323"/></svg>
  <div class="abs foot-name">Veltrasham College</div>
  <div class="abs foot-addr">12 Marlow Lane,<br>Ashbridge 4021</div>
  <div class="abs foot-dir">Click here to see the directions &gt;&gt;</div>

  <span class="abs foot-div" style="left:293px"></span>
  <div class="abs follow-title">Follow Us On:</div>
  <div class="abs social" style="left:352px"><i></i></div>
  <div class="abs social" style="left:386px"><i></i></div>
  <span class="abs foot-div" style="left:470px"></span>

  <div class="abs partner" style="left:505px;top:30px;width:68px;height:24px"></div>
  <div class="abs partner" style="left:590px;top:28px;width:70px;height:28px"></div>
  <div class="abs partner" style="left:497px;top:73px;width:84px;height:26px"></div>
  <div class="abs partner" style="left:590px;top:75px;width:72px;height:24px"></div>
  <div class="abs foot-seal"></div>
</footer>
<div class="copyright">Copyright © 2015 Veltrasham. All Rights Reserved.</div>

</body>
</html>
```